Business Card Design Project

I want a design for my business cards based on an excisting logo design.

Target Market(s)

Marketeers, PR-peeps, CEO's, decisionmakers, entrepreneurs

Industry/Entity Type

Business

Requirements
Nice to have
• Some visual interest on the back too
Should not have
• Sarif on the font

```html
<!DOCTYPE html>
<html lang="en">
<head>
<meta charset="utf-8">
<title>Leafline PR — Business Card</title>
<link rel="stylesheet" href="https://fonts.googleapis.com/css2?family=Cabin:wght@400;500;600;700&display=swap">
<style>
  :root {
    --stage: #3a3a3a;
    --lime: #a8cf38;
    --lime-light: #d6e86c;
    --lime-deep: #9fc72c;
    --green: #1f9e4a;
    --grey-text: #6f7174;
    --body-text: #4a4c4f;
    --paper: #e9eaea;
    --paper-light: #f3f3f3;
    --rule: #c9cbcb;
  }
  * { margin: 0; padding: 0; box-sizing: border-box; }
  html, body { width: 1200px; height: 960px; overflow: hidden; }
  body {
    background: var(--stage);
    font-family: "Cabin", "Segoe UI", sans-serif;
    position: relative;
  }
  .card { position: absolute; overflow: hidden; }

  /* Front */
  .card-front {
    left: 342px; top: 136px; width: 562px; height: 342px;
    background: radial-gradient(ellipse 60% 65% at 50% 42%, var(--lime-light) 0%, #c5de4f 45%, var(--lime-deep) 100%);
  }
  .front-mark {
    position: absolute; left: 236px; top: 100px;
    width: 88px; height: 88px; border-radius: 50%;
    background: #b6d648;
  }
  .front-name {
    position: absolute; left: 0; right: 0; top: 196px;
    text-align: center; font-size: 26px; font-weight: 500;
    letter-spacing: 1px; color: var(--grey-text);
  }
  .front-url {
    position: absolute; left: 0; right: 0; top: 229px;
    text-align: center; font-size: 13px; font-weight: 700; color: var(--green);
  }

  /* Back */
  .card-back {
    left: 342px; top: 539px; width: 566px; height: 337px;
    background: linear-gradient(135deg, var(--paper-light) 0%, var(--paper) 60%, #e2e3e3 100%);
  }
  .back-brand {
    position: absolute; left: 156px; top: 53px;
    display: flex; align-items: center; gap: 12px;
  }
  .back-brand .mark { width: 40px; height: 40px; border-radius: 50%; background: var(--lime); }
  .back-brand .name { font-size: 30px; font-weight: 500; letter-spacing: 1px; color: var(--grey-text); }
  .holder-name {
    position: absolute; right: 46px; top: 112px;
    font-size: 26px; font-weight: 600; color: var(--green);
  }
  .divider {
    position: absolute; left: 60px; width: 462px; top: 148px;
    border-top: 1px solid var(--rule);
  }
  .holder-role {
    position: absolute; right: 46px; top: 151px;
    font-size: 16px; color: var(--lime-deep);
  }
  .contact {
    position: absolute; left: 62px; top: 170px; list-style: none;
    font-size: 13px; color: var(--body-text); line-height: 17px;
  }
  .contact li { display: flex; align-items: flex-start; gap: 8px; }
  .contact li + li { margin-top: 1px; }
  .contact .gap { margin-top: 6px; }
  .contact svg { width: 12px; height: 12px; margin-top: 3px; flex: none; fill: var(--lime); }
  .wave { position: absolute; left: 0; top: 0; width: 566px; height: 337px; }
</style>
</head>
<body>
  <section class="card card-front" aria-label="Card front">
    <div class="front-mark"></div>
    <div class="front-name">Leafline PR</div>
    <div class="front-url">www.leaflinepr.com</div>
  </section>

  <section class="card card-back" aria-label="Card back">
    <svg class="wave" viewBox="0 0 566 337" aria-hidden="true">
      <path d="M0 286 C150 276 330 240 566 262 L566 337 L0 337 Z" fill="var(--lime)"/>
      <path d="M24 294 C180 284 360 246 566 268" fill="none" stroke="#ffffff" stroke-width="5"/>
      <path d="M28 290 C190 278 370 236 566 256 L566 264 C370 246 190 284 28 290 Z" fill="var(--green)"/>
    </svg>
    <div class="back-brand">
      <span class="mark"></span>
      <span class="name">Leafline PR</span>
    </div>
    <div class="holder-name">Marco Ellison</div>
    <div class="divider"></div>
    <div class="holder-role">Manager</div>
    <ul class="contact">
      <li>
        <svg viewBox="0 0 12 12"><path d="M6 1 L11.5 6 H10 V11 H7.2 V8 H4.8 V11 H2 V6 H0.5 Z"/></svg>
        <span>48 Harbor Lane, 12th Floor<br>Harbor building</span>
      </li>
      <li class="gap">
        <svg viewBox="0 0 12 12"><path d="M2.5 1 L4.5 1 L5.3 3.6 L4 4.6 C4.7 6.2 5.8 7.3 7.4 8 L8.4 6.7 L11 7.5 L11 9.5 C11 10.4 10.3 11 9.5 11 C5 10.6 1.4 7 1 2.5 C1 1.7 1.6 1 2.5 1 Z"/></svg>
        <span>0555 010 200 300</span>
      </li>
      <li>
        <svg viewBox="0 0 12 12"><path d="M0.5 2.5 H11.5 V9.5 H0.5 Z M1.2 3 L6 6.6 L10.8 3 Z" fill-rule="evenodd"/></svg>
        <span>marco@leaflinepr.com</span>
      </li>
      <li>
        <svg viewBox="0 0 12 12"><circle cx="6" cy="6" r="5"/></svg>
        <span>www.leaflinepr.com</span>
      </li>
    </ul>
  </section>
</body>
</html>
```